Clever & creative business card needed for a pediatric dentist.

We need a business card for a pediatric dentist that is building a brand-new pediatric dental practice. He is funny, outgoing, and sociable, and he hopes to give his business card to dentists and pediatricians so that he can give them information of where to refer infants, children, and teenagers that need high quality and attainable dental care.

The name of the dental practice is Copper Fern Pediatric Dentistry. Logo design .png / .pdf/ .jpg are provided to aid in the design.

The dentist's last name is Tolvan (which sounds like "burger", as in "hamburger” or “cheeseburger"). Since it is pediatric practice, kudos will be given to designs that implement a little joke into the design - but hopefully in a small or hidden way (such as putting something like a cheeseburger on the back of the card, or hiding it an an abstract way).

Thank you!

Please make a design that incorporates colors. It should be fun! Not too serious. It does not have to follow the color scheme of the logos.

```html
<!DOCTYPE html>
<html lang="en">
<head>
<meta charset="utf-8">
<title>Copper Fern Pediatric Dentistry – Business Card</title>
<link rel="stylesheet" href="https://fonts.googleapis.com/css2?family=Montserrat:wght@700&family=Nunito+Sans:wght@300;400;700&display=swap">
<style>
  :root {
    --backdrop: #e8e8e9;
    --card-dark: #474747;
    --card-light: #ffffff;
    --green-deep: #2f9a45;
    --green-mid: #5cb85f;
    --green-soft: #9fd39b;
    --green-pale: #d8eed5;
    --ink: #4a4a4a;
    --ink-soft: #6a6a6a;
  }
  * { box-sizing: border-box; margin: 0; padding: 0; }
  html, body { width: 1200px; height: 794px; overflow: hidden; }
  body {
    background: var(--backdrop);
    font-family: "Nunito Sans", Arial, sans-serif;
    position: relative;
  }
  .card {
    position: absolute;
    top: 248px;
    width: 525px;
    height: 300px;
    box-shadow: 0 2px 6px rgba(0,0,0,.12);
    overflow: hidden;
  }
  /* Front */
  .card--front { left: 45px; background: var(--card-dark); }
  .front-brand {
    position: absolute;
    left: 0; right: 0; top: 104px;
    display: flex; align-items: center; justify-content: center; gap: 14px;
  }
  .brand-dot {
    width: 38px; height: 38px; border-radius: 50%;
    background: var(--green-mid);
    flex: none;
  }
  .brand-name {
    font-family: "Nunito Sans", Arial, sans-serif;
    font-weight: 400;
    line-height: 1.15;
  }
  .front-brand .brand-name { color: #ffffff; font-size: 26px; }
  .front-brand .brand-name small { display: block; font-size: 26px; }
  .stripe {
    position: absolute; left: 0; right: 0; bottom: 0; height: 16px;
    display: flex;
  }
  .stripe span { flex: 1; }
  .stripe span:nth-child(1) { background: var(--green-pale); }
  .stripe span:nth-child(2) { background: var(--green-soft); }
  .stripe span:nth-child(3) { background: var(--green-mid); }
  .stripe span:nth-child(4) { background: var(--green-deep); }

  /* Back */
  .card--back { left: 630px; background: var(--card-light); }
  .back-brand {
    position: absolute; right: 28px; top: 26px;
    display: flex; align-items: center; gap: 10px;
  }
  .back-brand .brand-dot { width: 28px; height: 28px; }
  .back-brand .brand-name { color: var(--ink); font-size: 15px; text-align: left; }
  .burger-art {
    position: absolute; left: 118px; top: 76px;
    width: 118px; height: 82px; border-radius: 46px 46px 16px 16px;
    background: linear-gradient(180deg, var(--green-pale), #eef7ec);
  }
  .doctor-name {
    position: absolute; left: 44px; top: 116px;
    font-family: "Montserrat", Arial, sans-serif; font-weight: 700;
    font-size: 19px; color: var(--green-deep); letter-spacing: .2px;
  }
  .contact-list {
    position: absolute; left: 44px; top: 172px;
    list-style: none; color: var(--ink-soft); font-size: 14px; font-weight: 300;
  }
  .contact-list li { display: flex; align-items: center; gap: 12px; height: 26px; }
  .contact-list svg { width: 16px; height: 16px; flex: none; stroke: var(--green-mid); fill: none; stroke-width: 1.4; stroke-linecap: round; stroke-linejoin: round; }
  .contact-list b { font-weight: 700; color: var(--ink); }
  .phone-pair { display: flex; align-items: center; gap: 8px; }
</style>
</head>
<body>
  <section class="card card--front" aria-label="Card front">
    <div class="front-brand">
      <span class="brand-dot"></span>
      <p class="brand-name">Copper Fern<small>Pediatric Dentistry</small></p>
    </div>
    <div class="stripe"><span></span><span></span><span></span><span></span></div>
  </section>

  <section class="card card--back" aria-label="Card back">
    <div class="back-brand">
      <span class="brand-dot"></span>
      <p class="brand-name">Copper Fern<br>Pediatric Dentistry</p>
    </div>
    <div class="burger-art" role="img" aria-label="Light green outline drawing of a cheeseburger behind the dentist's name"></div>
    <h1 class="doctor-name">DORIAN TOLVAN, D.M.D.</h1>
    <ul class="contact-list">
      <li>
        <svg viewBox="0 0 16 16"><rect x="4.5" y="1.5" width="7" height="13" rx="1.2"/><line x1="7" y1="12" x2="9" y2="12"/></svg>
        <span class="phone-pair">407.555.0182
          <svg viewBox="0 0 16 16"><path d="M3 2.5l2.5-.5 1.5 3-1.5 1.2a8 8 0 0 0 3.8 3.8L10.5 8.5l3 1.5-.5 2.5c-.3.8-1 1.2-1.8 1A11 11 0 0 1 2 3.8c-.2-.8.2-1.3 1-1.3z"/></svg>
          321.555.0146</span>
      </li>
      <li>
        <svg viewBox="0 0 16 16"><rect x="1.5" y="3.5" width="13" height="9" rx="1"/><path d="M1.8 4l6.2 5 6.2-5"/></svg>
        <span>dorian.tolvan.dmd@mailbox.com</span>
      </li>
      <li>
        <svg viewBox="0 0 16 16"><circle cx="8" cy="8" r="6.5"/><path d="M1.5 8h13M8 1.5c2 2 2 11 0 13M8 1.5c-2 2-2 11 0 13"/></svg>
        <span>www.<b>COPPERFERN</b>.com</span>
      </li>
      <li>
        <svg viewBox="0 0 16 16"><path d="M8 14.5s-4.5-4.6-4.5-8a4.5 4.5 0 0 1 9 0c0 3.4-4.5 8-4.5 8z"/><circle cx="8" cy="6.5" r="1.6"/></svg>
        <span>418 Linden Row, Fairview, CT, 06900</span>
      </li>
    </ul>
  </section>
</body>
</html>
```